Need Business Card for our Real Estate Business with Sales Executive's Picture

PANTONE 484 C ( RED)

PANTONE 2766 C ( BLUE

Industry/Entity Type

Real Estate

Contact Information for Business Card

Name, Mobile, email, & picture of Person
Agency Phone, address, Web address

Requirements
Must have
• Our Logo Colours, Agent Picture,

```html
<!DOCTYPE html>
<html lang="en">
<head>
<meta charset="utf-8">
<title>Dunmore Realty – Business Card</title>
<link href="https://fonts.googleapis.com/css2?family=Work+Sans:wght@400;500;700&display=swap" rel="stylesheet">
<style>
  :root {
    --navy: #0b1640;
    --white: #ffffff;
    --stage: #d4d4d6;
    --accent-red: #8b1a1a;
    --photo-top: #2a3a78;
    --photo-bottom: #c9a58c;
  }
  * { margin: 0; padding: 0; box-sizing: border-box; }
  html, body { width: 1200px; height: 800px; overflow: hidden; }
  body {
    background: var(--stage);
    font-family: "Work Sans", Arial, sans-serif;
    position: relative;
  }
  .card {
    position: absolute;
    top: 240px;
    width: 540px;
    height: 308px;
    box-shadow: 0 6px 18px rgba(0,0,0,.18);
    overflow: hidden;
  }
  .card--front { left: 40px; background: var(--white); }
  .card--back  { left: 620px; background: var(--navy); }

  .front-band { position: absolute; inset: 0; width: 100%; height: 100%; }

  .agent-photo {
    position: absolute;
    left: 200px; top: 30px;
    width: 112px; height: 112px;
    border-radius: 50%;
    border: 2px solid var(--navy);
    background: linear-gradient(180deg, var(--photo-top) 0%, var(--photo-bottom) 100%);
  }

  .agent-details {
    position: absolute;
    left: 28px; bottom: 22px;
    color: var(--white);
  }
  .agent-name { font-weight: 700; font-size: 19px; letter-spacing: .3px; text-transform: uppercase; }
  .agent-role { font-size: 13px; margin-top: 2px; }
  .agent-address { font-size: 12.5px; margin-top: 10px; line-height: 1.4; }

  .contact-list {
    position: absolute;
    right: 24px; top: 126px;
    list-style: none;
    color: var(--white);
    font-size: 12px;
    line-height: 1.6;
  }
  .contact-list li { display: flex; align-items: center; gap: 7px; }
  .contact-list svg { width: 10px; height: 10px; fill: var(--white); flex: none; }

  .brand-mark {
    position: absolute;
    right: 24px; bottom: 24px;
    display: flex; align-items: center; gap: 8px;
    color: var(--white);
    font-size: 13px; font-weight: 500; letter-spacing: 2px;
  }
  .brand-mark .dot { width: 8px; height: 8px; background: var(--accent-red); }

  .back-brand {
    position: absolute; inset: 0;
    display: flex; align-items: center; justify-content: center; gap: 14px;
    color: var(--white);
    font-size: 34px; font-weight: 500; letter-spacing: 6px;
  }
  .back-brand .square { width: 14px; height: 14px; background: var(--white); }
</style>
</head>
<body>

  <section class="card card--front">
    <svg class="front-band" viewBox="0 0 540 308" preserveAspectRatio="none" aria-hidden="true">
      <polygon points="0,190 290,190 362,112 540,112 540,308 0,308" fill="var(--navy)"/>
      <polyline points="300,308 392,224 540,224" fill="none" stroke="var(--white)" stroke-width="2"/>
    </svg>

    <div class="agent-photo" role="img" aria-label="Portrait photo of the agent in a navy suit"></div>

    <div class="agent-details">
      <p class="agent-name">Daniel Reyes</p>
      <p class="agent-role">Managing Director</p>
      <p class="agent-address">Via dei Pini, 14.<br>12030 Lagnasco (CN)</p>
    </div>

    <ul class="contact-list">
      <li><svg viewBox="0 0 10 10"><path d="M2 0h2l1 3-1.4 1a6 6 0 0 0 2.4 2.4L7 5l3 1v2a2 2 0 0 1-2 2A8 8 0 0 1 0 2a2 2 0 0 1 2-2z"/></svg>+852 3100 4417</li>
      <li><svg viewBox="0 0 10 10"><rect x="2" y="0" width="6" height="10" rx="1"/></svg>+852 3100 4418</li>
      <li><svg viewBox="0 0 10 10"><path d="M0 2h10v6H0z M0 2l5 3 5-3" fill="none" stroke="#fff" stroke-width="1"/></svg>info@dunmorerealty.com</li>
      <li><svg viewBox="0 0 10 10"><circle cx="5" cy="5" r="4.3" fill="none" stroke="#fff" stroke-width="1"/><path d="M1 5h8M5 1v8" stroke="#fff" stroke-width="1"/></svg>www.dunmorerealty.com</li>
    </ul>

    <div class="brand-mark"><span class="dot"></span>DUNMORE REALTY</div>
  </section>

  <section class="card card--back">
    <div class="back-brand"><span class="square"></span>DUNMORE REALTY</div>
  </section>

</body>
</html>
```